ターゲットは、墓地を探している方です。生前墓、小規模墓地、ペットと共に墓地に入れる敷地も用意されています。
http://www.asahidaireien.jp/
1ページ
緑 青
• イラストレーター形式 (.ai)
サイトレイアウトのPDFデータです。

弊社お客様にデザインを選んでいただきました。
お客様のイメージと一致したようでとても喜んでいただきました。

すばらしいデザインをありがとうございました。
24デザインの中からお客様に選んでいただきました。
お客様はとても喜んでおります。
今後ともよろしくお願いします。

```html
<!DOCTYPE html>
<html lang="ja">
<head>
<meta charset="utf-8">
<title>朝日台霊園</title>
<link rel="stylesheet" href="https://fonts.googleapis.com/css2?family=Noto+Sans+JP:wght@400;700&family=Noto+Serif+JP:wght@500;700&display=swap">
<style>
:root{
  --green-dark:#17461f;
  --green:#2e6b2c;
  --green-mid:#4d8a3a;
  --green-light:#8fb96b;
  --green-pale:#eef3e4;
  --teal:#2f7f8a;
  --teal-light:#5fa9b0;
  --line:#c9d8b6;
  --text:#3b3b3b;
  --muted:#6a6a6a;
  --white:#fff;
  --cream:#fbfaf3;
}
*{box-sizing:border-box;margin:0;padding:0}
html,body{width:701px;height:1200px;overflow:hidden}
body{font-family:"Noto Sans JP",sans-serif;color:var(--text);font-size:8px;line-height:1.5;
  background:var(--green-pale) repeating-linear-gradient(45deg,rgba(255,255,255,.35) 0 2px,transparent 2px 6px)}
.site{width:701px;height:1200px;position:relative}
.wrap{width:600px;margin:0 auto;position:relative}

/* header */
.header{height:48px;background:var(--white)}
.header .wrap{height:48px;display:flex;justify-content:space-between;align-items:center}
.brand{display:flex;align-items:center;gap:6px}
.brand-mark{width:14px;height:14px;background:var(--green-light)}
.brand-tag{font-size:7px;color:var(--green);display:block;line-height:1}
.brand-name{font-family:"Noto Serif JP",serif;font-weight:700;font-size:20px;color:var(--green);line-height:1.1;letter-spacing:2px}
.contact{text-align:right}
.contact-label{font-size:7px;color:var(--green);display:block}
.contact-tel{display:flex;align-items:center;gap:4px;font-size:22px;font-weight:700;color:var(--green);line-height:1}

/* nav */
.nav{height:22px;background:linear-gradient(var(--green-mid),var(--green-dark))}
.nav ul{list-style:none;display:flex;height:22px;width:600px;margin:0 auto}
.nav li{flex:1;text-align:center;color:var(--white);font-size:8px;line-height:22px;border-right:1px solid rgba(255,255,255,.25)}
.nav li:first-child{border-left:1px solid rgba(255,255,255,.25)}

/* hero */
.hero{height:178px;position:relative;overflow:hidden}
.hero-photo{position:absolute;inset:0;background:linear-gradient(180deg,#cfe3f2 0%,#e7f0f4 38%,#9fbf86 62%,#7a8f72 80%,#b7bdb4 100%)}
.hero-flowers{position:absolute;right:0;top:0;width:210px;height:178px;background:radial-gradient(circle at 60% 40%,#e86aa0 0,#c77fd0 30%,#8fc05a 62%,rgba(143,192,90,0) 80%)}
.hero-copy{position:absolute;left:60px;top:22px}
.hero-copy h1{font-family:"Noto Serif JP",serif;font-weight:700;font-size:20px;color:var(--green-dark);letter-spacing:1px}
.hero-copy p{font-size:8px;color:var(--green-dark);margin-top:2px}

/* body columns */
.main{display:flex;gap:12px;padding-top:14px;height:835px}
.side{width:170px;display:flex;flex-direction:column;gap:12px}
.content{width:418px;display:flex;flex-direction:column;gap:10px}

.box{background:var(--cream);border:1px solid var(--line)}
.box-head{height:22px;padding:0 8px;display:flex;align-items:center;justify-content:space-between;
  font-family:"Noto Serif JP",serif;font-weight:700;font-size:10px;color:var(--green)}
.box-head.band{background:linear-gradient(var(--green-mid),var(--green));color:var(--white);font-size:9px}
.box-body{padding:6px 8px}
.voice{padding:5px 0;border-bottom:1px dotted var(--line)}
.voice h3{font-size:8px;color:var(--green);font-weight:700}
.voice p{font-size:7px;color:var(--muted);line-height:1.45}
.voice-people{width:46px;height:18px;background:linear-gradient(90deg,#f0c7b5,#e9d6a8)}
.more{display:block;text-align:right;font-size:7px;color:var(--green);margin-top:5px}
.btn{display:inline-block;background:var(--green-mid);color:var(--white);font-size:7px;padding:2px 8px;border-radius:2px}

.facility{display:flex;gap:6px}
.facility-photo{width:70px;height:80px;background:linear-gradient(#bcd7e8,#9bb98b 60%,#8c8c80)}
.facility p{font-size:7px;color:var(--muted);flex:1}

.access-photo{height:86px;background:linear-gradient(#cfe2ee,#98b482 55%,#a9aba3)}
.access p{font-size:7px;color:var(--muted);margin-top:5px}
.access .btn{margin-top:6px;display:block;text-align:center}
.address{margin-top:8px;font-size:7px;line-height:1.6}
.address strong{color:var(--green);font-size:8px}

.intro{display:flex;padding:10px;gap:10px;background:var(--white)}
.intro-text{flex:1}
.intro h2{font-family:"Noto Serif JP",serif;font-size:13px;color:var(--green);margin-bottom:4px}
.intro p{font-size:7px;color:var(--muted)}
.intro-photo{width:150px;height:100px;background:linear-gradient(135deg,#e7eef3,#d8e7c6 60%,#c2d7a6)}
.intro .btn{margin-top:8px}

.section-head{height:24px;background:linear-gradient(var(--teal-light),var(--teal));color:var(--white);
  display:flex;align-items:center;gap:6px;padding:0 10px;font-family:"Noto Serif JP",serif;font-weight:700;font-size:11px}
.section-head svg{flex:none}
.topics{background:var(--white);border:1px solid var(--line);padding:4px 10px}
.topic{display:flex;gap:10px;padding:10px 0;border-bottom:1px dotted var(--line)}
.topic:last-child{border-bottom:none}
.topic-photo{width:92px;height:80px;flex:none}
.t1{background:linear-gradient(#dbe7ee,#a7bf93 55%,#98958b)}
.t2{background:radial-gradient(circle,#b65fb8,#7d3f8e 70%,#5c7c48)}
.t3{background:linear-gradient(#e0eaf0,#b8c6a6 55%,#8d8e86)}
.topic h3{font-size:9px;color:var(--teal);font-weight:700;margin-bottom:3px}
.topic h3::before{content:"■ ";color:var(--green-mid);font-size:7px}
.topic p{font-size:7px;color:var(--muted)}

.news{background:var(--white);border:1px solid var(--line)}
.news .box-head{border-bottom:2px solid var(--green-mid);color:var(--green)}
.news .box-head span{font-family:"Noto Sans JP",sans-serif;font-weight:400;font-size:7px}
.news table{width:100%;border-collapse:collapse;font-size:7px}
.news td{padding:5px 8px;border-bottom:1px dotted var(--line)}
.news td.date{width:70px;color:var(--green)}
.pagetop{text-align:right;font-size:7px;color:var(--green);margin-top:4px}

/* footer */
.footer{position:absolute;left:0;right:0;bottom:0;height:120px;background:var(--green-dark);color:var(--white)}
.footer::before{content:"";display:block;height:4px;background:var(--green-mid)}
.footer .wrap{display:flex;justify-content:space-between;padding-top:12px}
.f-brand .brand-tag{color:#cfe2bf}
.f-brand .brand-name{color:var(--white);font-size:18px}
.f-brand p{font-size:7px;line-height:1.55;margin-top:3px}
.f-tel{font-size:13px;font-weight:700;margin-top:2px;display:flex;align-items:center;gap:3px}
.f-links{font-size:7px;text-align:right;line-height:1.8;margin-top:4px}
.copyright{position:absolute;bottom:6px;left:0;right:0;text-align:center;font-size:6.5px;color:#b9cfae}
</style>
</head>
<body>
<div class="site">
  <header class="header">
    <div class="wrap">
      <div class="brand">
        <span class="brand-mark"></span>
        <div>
          <span class="brand-tag">やすらぎの公園墓地</span>
          <span class="brand-name">朝日台霊園</span>
        </div>
      </div>
      <div class="contact">
        <span class="contact-label">お客様の窓口</span>
        <div class="contact-tel">
          <svg width="20" height="14" viewBox="0 0 20 14"><rect width="20" height="14" rx="2" fill="#2e6b2c"/><path d="M6 3c1 0 1.5 2 1 2.5L6.3 6.3c.6 1.4 1.6 2.4 3 3l.8-.7c.5-.5 2.5 0 2.5 1 0 1-1 1.6-2 1.4C7.7 10.5 4.5 7.3 4 4.5 3.9 3.6 5 3 6 3z" fill="#fff"/></svg>
          0120-48-7210
        </div>
      </div>
    </div>
  </header>

  <nav class="nav">
    <ul>
      <li>HOME</li><li>墓地施設の紹介</li><li>アクセス・地図</li><li>墓地の手続き</li><li>区画案内</li><li>墓石紹介</li><li>お問い合わせ</li>
    </ul>
  </nav>

  <section class="hero">
    <div class="hero-photo" role="img" aria-label="青空の下に広がる霊園の墓石の並び"></div>
    <div class="hero-flowers" role="img" aria-label="色とりどりの供花"></div>
    <div class="hero-copy">
      <h1>ご先祖様との語らいの聖地。</h1>
      <p>やすらぎの緑に包まれた、心穏やかにお参りできる公園墓地です。</p>
    </div>
  </section>

  <div class="wrap">
    <div class="main">
      <aside class="side">
        <div class="box">
          <div class="box-head">お客様の声<span class="voice-people" role="img" aria-label="家族のイラスト"></span></div>
          <div class="box-body">
            <div class="voice">
              <h3>家族墓地のお客様</h3>
              <p>緑が多く明るい雰囲気で、家族みんなが安心してお参りできます。スタッフの方の対応もとても丁寧でした。</p>
            </div>
            <div class="voice">
              <h3>生前墓のお客様</h3>
              <p>元気なうちに自分で選べて良かったです。手続きもわかりやすく説明していただきました。</p>
            </div>
            <div class="voice">
              <h3>ペット墓地のお客様</h3>
              <p>愛犬と一緒に眠れる区画があり、とても嬉しく思います。管理も行き届いています。</p>
            </div>
            <span class="more">» 続きを見る</span>
          </div>
        </div>

        <div class="box">
          <div class="box-head">園内施設</div>
          <div class="box-body facility">
            <div class="facility-photo" role="img" aria-label="園内の休憩所の建物"></div>
            <p>休憩所や水場、駐車場を完備しております。ご年配の方も安心してお参りいただけるよう、園内は段差の少ない造りです。</p>
          </div>
        </div>

        <div class="box access">
          <div class="box-head band">朝日台霊園へのアクセス</div>
          <div class="box-body">
            <div class="access-photo" role="img" aria-label="霊園入口の外観"></div>
            <p>最寄り駅より車で約10分。無料送迎バスもご用意しております。お気軽にお問い合わせください。</p>
            <span class="btn">» 詳しい地図を見る</span>
            <div class="address">
              <strong>朝日台霊園</strong><br>
              〒000-1234<br>
              緑ヶ丘市朝日台3-12-1<br>
              TEL 0000-12-3456<br>
              FAX 0000-12-3457
            </div>
          </div>
        </div>
      </aside>

      <main class="content">
        <div class="box intro">
          <div class="intro-text">
            <h2>朝日台霊園</h2>
            <p>四季折々の自然に囲まれた公園墓地です。生前墓や小規模墓地のほか、ペットと共に入れる区画もご用意しております。宗教・宗派を問わずご利用いただけます。ご見学はいつでも受け付けております。</p>
            <span class="btn">» 詳しく見る</span>
          </div>
          <div class="intro-photo" role="img" aria-label="墓参りに訪れた家族の様子"></div>
        </div>

        <div>
          <div class="section-head">
            <svg width="12" height="12" viewBox="0 0 12 12"><rect x="3" y="1" width="6" height="8" fill="#fff"/><rect x="1" y="9" width="10" height="2" fill="#fff"/></svg>
            墓地について
          </div>
          <div class="topics">
            <div class="topic">
              <div class="topic-photo t1" role="img" aria-label="整然と並ぶ墓石"></div>
              <div>
                <h3>霊園と墓地の違い</h3>
                <p>霊園とは宗教や宗派を問わず利用できる墓地のことです。寺院墓地とは異なり、檀家になる必要がありません。管理体制や費用の仕組みについても、わかりやすくご説明いたします。お墓選びの第一歩としてご覧ください。</p>
              </div>
            </div>
            <div class="topic">
              <div class="topic-photo t2" role="img" aria-label="紫色の花の写真"></div>
              <div>
                <h3>ここにタイトルが入ります</h3>
                <p>ここに説明文が入ります。ここに説明文が入ります。ここに説明文が入ります。ここに説明文が入ります。ここに説明文が入ります。ここに説明文が入ります。ここに説明文が入ります。</p>
              </div>
            </div>
            <div class="topic">
              <div class="topic-photo t3" role="img" aria-label="霊園の区画の風景"></div>
              <div>
                <h3>ここにタイトルが入ります</h3>
                <p>ここに説明文が入ります。ここに説明文が入ります。ここに説明文が入ります。ここに説明文が入ります。ここに説明文が入ります。ここに説明文が入ります。ここに説明文が入ります。</p>
              </div>
            </div>
          </div>
        </div>

        <div class="news">
          <div class="box-head">最新のお知らせ<span>» 一覧を見る</span></div>
          <table>
            <tr><td class="date">2011.01.26</td><td>ペット墓地の区画を新設いたしました</td></tr>
            <tr><td class="date">2011.02.10</td><td>春のお彼岸の合同法要のご案内</td></tr>
            <tr><td class="date">2011.02.14</td><td>ホームページをリニューアルしました</td></tr>
            <tr><td class="date">2011.02.17</td><td>園内施設の改修工事のお知らせ</td></tr>
          </table>
        </div>

        <p class="pagetop">▲ ページの先頭へ戻る</p>
      </main>
    </div>
  </div>

  <footer class="footer">
    <div class="wrap">
      <div class="f-brand">
        <span class="brand-tag">やすらぎの公園墓地</span>
        <span class="brand-name">朝日台霊園</span>
        <p>朝日台霊園 管理事務所<br>〒000-1234 緑ヶ丘市朝日台3-12-1<br>TEL 0000-12-3456 / FAX 0000-12-3457</p>
        <div class="f-tel">
          <svg width="14" height="10" viewBox="0 0 20 14"><rect width="20" height="14" rx="2" fill="#fff"/><path d="M6 3c1 0 1.5 2 1 2.5L6.3 6.3c.6 1.4 1.6 2.4 3 3l.8-.7c.5-.5 2.5 0 2.5 1 0 1-1 1.6-2 1.4C7.7 10.5 4.5 7.3 4 4.5 3.9 3.6 5 3 6 3z" fill="#17461f"/></svg>
          0120-48-7210
        </div>
      </div>
      <div class="f-links">
        | HOME | 墓地施設の紹介 | アクセス・地図 | 墓地の手続き | 区画案内 |<br>
        | 墓石紹介 | お問い合わせ | サイトマップ | プライバシーポリシー |
      </div>
    </div>
    <p class="copyright">Copyright(C) Asahidaireien. All Rights Reserved.</p>
  </footer>
</div>
</body>
</html>
```